CALDERWYN STATIONARY
CALDRWYN STATIONARY
CALDERWYN STATIONARY -
Creative Brief
Professional
KHALID R AL-MUTAWA
CEO
P.O.BOX: 57384 RIYADH: 12958 KINGDOM OF SAUDI ARABIA
kalmutawa@mailvero.com
www.calderwyn-example.com

```html
<!DOCTYPE html>
<html lang="en">
<head>
<meta charset="utf-8">
<title>Calderwyn Stationery</title>
<link href="https://fonts.googleapis.com/css2?family=Montserrat:wght@400;600&display=swap" rel="stylesheet">
<style>
:root{
  --board:#3a3a3c;
  --paper:#ffffff;
  --gold:#c9a03a;
  --gold-light:#ecd38a;
  --gold-dark:#9c7420;
  --ink:#5a5a5a;
  --caption:#c8c8c8;
}
*{margin:0;padding:0;box-sizing:border-box}
html,body{width:1200px;height:338px;overflow:hidden}
body{background:var(--board);font-family:'Montserrat',sans-serif;position:relative}
.item{position:absolute;background:var(--paper);overflow:hidden;box-shadow:0 2px 6px rgba(0,0,0,.45)}
.item svg.curve{position:absolute;left:0;top:0;width:100%;height:100%}
.brand{position:absolute;display:flex;align-items:center;gap:3px;font-weight:600;color:var(--gold-dark);letter-spacing:.5px;white-space:nowrap}
.brand .mark{background:var(--gold);display:block}
.caption{position:absolute;font-size:5px;color:var(--caption);text-align:center;white-space:nowrap}
.tiny{position:absolute;font-size:3.2px;color:var(--ink);line-height:1.35;white-space:nowrap}
.watermark{position:absolute;background:var(--gold-light);opacity:.18;transform:rotate(45deg)}
</style>
</head>
<body>
<svg width="0" height="0" style="position:absolute">
  <defs>
    <linearGradient id="goldFill" x1="0" y1="0" x2="1" y2="1">
      <stop offset="0" stop-color="#9c7420"/><stop offset=".45" stop-color="#ecd38a"/><stop offset="1" stop-color="#b8862a"/>
    </linearGradient>
    <linearGradient id="silverFill" x1="0" y1="0" x2="1" y2="0">
      <stop offset="0" stop-color="#8a8a8c"/><stop offset=".5" stop-color="#e2e2e4"/><stop offset="1" stop-color="#8a8a8c"/>
    </linearGradient>
  </defs>
</svg>

<div class="item business-card-front" style="left:19px;top:199px;width:91px;height:41px">
  <svg class="curve" viewBox="0 0 91 41" preserveAspectRatio="none"><path d="M0 30 Q40 36 91 26 L91 41 L0 41Z" fill="url(#goldFill)"/></svg>
  <div class="brand" style="left:6px;top:8px;font-size:5px"><span class="mark" style="width:5px;height:5px"></span>CALDERWYN</div>
  <div class="tiny" style="left:6px;top:17px">MANAGING DIRECTOR</div>
</div>
<div class="caption" style="left:19px;top:242px;width:91px">Business Card Front</div>

<div class="item business-card-back" style="left:19px;top:257px;width:91px;height:41px">
  <svg class="curve" viewBox="0 0 91 41" preserveAspectRatio="none"><path d="M0 0 L91 0 L91 12 Q45 4 0 14Z" fill="url(#goldFill)"/></svg>
  <div class="tiny" style="left:6px;top:20px">TEL: 011 000 0000<br>info@calderwyn-example.com<br>www.calderwyn-example.com</div>
</div>
<div class="caption" style="left:19px;top:300px;width:91px">Business Card Back</div>

<div class="item letterhead" style="left:134px;top:38px;width:233px;height:281px">
  <svg class="curve" viewBox="0 0 233 281" preserveAspectRatio="none">
    <path d="M0 0 L14 0 Q8 120 0 150Z" fill="url(#goldFill)"/>
    <path d="M0 281 L0 250 Q110 262 233 236 L233 281Z" fill="url(#goldFill)"/>
    <path d="M0 246 Q110 256 233 230" stroke="var(--gold)" stroke-width=".8" fill="none"/>
  </svg>
  <div class="watermark" style="left:80px;top:95px;width:72px;height:72px"></div>
  <div class="brand" style="left:92px;top:18px;font-size:6px"><span class="mark" style="width:6px;height:6px"></span>CALDERWYN</div>
  <div class="tiny" style="left:0;width:233px;text-align:center;top:270px;color:#fff">TEL: 011 000 0000 | info@calderwyn-example.com | www.calderwyn-example.com</div>
</div>
<div class="caption" style="left:134px;top:322px;width:233px">Letterhead Page One</div>

<div class="item letterhead" style="left:384px;top:38px;width:233px;height:281px">
  <svg class="curve" viewBox="0 0 233 281" preserveAspectRatio="none">
    <path d="M0 281 L0 258 Q120 268 233 244 L233 281Z" fill="url(#goldFill)"/>
    <path d="M0 254 Q120 264 233 238" stroke="var(--gold)" stroke-width=".8" fill="none"/>
  </svg>
  <div class="watermark" style="left:80px;top:95px;width:72px;height:72px"></div>
  <div class="brand" style="left:14px;top:16px;font-size:6px"><span class="mark" style="width:6px;height:6px"></span>CALDERWYN</div>
  <div class="tiny" style="left:160px;top:16px">TEL: 011 000 0000<br>info@calderwyn-example.com<br>www.calderwyn-example.com</div>
</div>
<div class="caption" style="left:384px;top:322px;width:233px">Letterhead Page Two</div>

<div class="item envelope-front" style="left:631px;top:46px;width:262px;height:127px">
  <svg class="curve" viewBox="0 0 262 127" preserveAspectRatio="none">
    <path d="M0 127 L0 110 Q130 120 262 96 L262 127Z" fill="url(#goldFill)"/>
    <path d="M0 106 Q130 116 262 90" stroke="var(--gold)" stroke-width=".8" fill="none"/>
  </svg>
  <div class="brand" style="left:12px;top:12px;font-size:5.5px"><span class="mark" style="width:5px;height:5px"></span>CALDERWYN</div>
</div>
<div class="caption" style="left:631px;top:175px;width:262px">Envelope Front</div>

<div class="item compliment-slip" style="left:631px;top:182px;width:262px;height:118px">
  <svg class="curve" viewBox="0 0 262 118" preserveAspectRatio="none">
    <path d="M0 0 L10 0 Q6 60 0 80Z" fill="url(#goldFill)"/>
    <path d="M0 118 L0 102 Q130 112 262 88 L262 118Z" fill="url(#goldFill)"/>
  </svg>
  <div class="brand" style="left:20px;top:12px;font-size:5.5px"><span class="mark" style="width:5px;height:5px"></span>CALDERWYN</div>
</div>
<div class="caption" style="left:631px;top:302px;width:262px">Compliment Slip</div>

<div class="item envelope-back-gold" style="left:912px;top:43px;width:271px;height:65px">
  <svg class="curve" viewBox="0 0 271 65" preserveAspectRatio="none"><path d="M0 0 L271 0 L271 8 L135 62 L0 8Z" fill="url(#goldFill)"/></svg>
</div>
<div class="item envelope-back-silver" style="left:912px;top:158px;width:271px;height:46px">
  <svg class="curve" viewBox="0 0 271 46" preserveAspectRatio="none"><path d="M0 0 L271 0 L271 6 L135 44 L0 6Z" fill="url(#silverFill)"/></svg>
</div>
<div class="item envelope-back-white" style="left:912px;top:216px;width:271px;height:86px">
  <svg class="curve" viewBox="0 0 271 86" preserveAspectRatio="none"><path d="M0 0 L135 40 L271 0" stroke="#d6d6d6" stroke-width="1" fill="none"/></svg>
  <span style="position:absolute;left:131px;top:22px;width:8px;height:8px;background:var(--gold)"></span>
</div>
<div class="caption" style="left:912px;top:306px;width:271px">Envelope Back Views</div>
</body>
</html>
```